Verpackungsdesign für Glasprodukte
Zielgruppe
Wir sind eine Glaser Handwerksunternehmen die Dienstleistung und Glasprodukte verkaufen, unsere Zielgruppe sind BtoB und BtoC Kunden an die wir hochwertige Produkte für faire Preise anbieten.
Aufgabenstellung
Schlichtes und modernes Design, auf der Vorderseite soll das Logo, innen kommt eine Persönlicher Text und ein Bild von mir

```html
<!DOCTYPE html>
<html lang="de">
<head>
<meta charset="utf-8">
<title>Glaserei Talbunor – Mappe</title>
<link href="https://fonts.googleapis.com/css2?family=Nunito+Sans:wght@300;400;600;700&display=swap" rel="stylesheet">
<style>
:root{
  --bg:#d9d9d9;
  --paper:#f2f2f2;
  --taupe:#a59d93;
  --ink:#5a5754;
  --ink-dark:#3c3a38;
  --ink-soft:#8a8785;
  --white:#ffffff;
}
*{margin:0;padding:0;box-sizing:border-box}
html,body{width:1200px;height:1200px;overflow:hidden;background:var(--bg);font-family:"Nunito Sans",sans-serif;color:var(--ink)}
.spread{position:absolute;left:60px;width:1080px;height:510px;display:flex;box-shadow:0 10px 30px rgba(0,0,0,.18)}
.spread--inside{top:45px}
.spread--outside{top:635px}
.panel{position:relative;width:360px;height:100%;background:var(--paper);overflow:hidden}
.panel+.panel{border-left:1px solid #dcdcdc}
.band{position:absolute;left:0;right:0;bottom:0;height:48px;background:var(--taupe);color:var(--white);font-size:11px;display:flex;align-items:center;justify-content:center;letter-spacing:.02em}
.brand{display:flex;align-items:center;gap:10px;font-weight:600;font-size:17px;color:var(--ink);letter-spacing:.04em;white-space:nowrap}
.brand__square{width:14px;height:14px;background:var(--taupe);flex:none}
.glass-art{position:absolute;left:30px;top:70px;width:290px;height:330px;background:linear-gradient(135deg,#fafafa 0%,#cfcfcf 55%,#a9a9a9 100%)}
.glass-art .brand{position:absolute;left:50%;top:50%;transform:translate(-50%,-50%)}
.web{font-weight:700;font-size:17px;color:var(--ink);text-align:center;letter-spacing:.02em}
.social{display:flex;justify-content:center;gap:10px;margin-top:12px}
.social span{width:22px;height:22px;border-radius:50%;background:var(--ink)}
.center-block{position:absolute;left:0;right:0;top:175px}
.pocket{position:absolute;left:20px;right:20px;bottom:0;height:86px;background:var(--taupe);clip-path:polygon(3% 0,97% 0,100% 100%,0 100%)}
.pocket__pattern{position:absolute;left:0;right:0;top:0;height:38px;background:linear-gradient(180deg,#eeeeee,#e2e2e2)}
.pocket__mail{position:absolute;right:22px;bottom:15px;font-size:10px;color:var(--white);white-space:nowrap}
.card{position:absolute;left:36px;bottom:16px;width:112px;height:88px;background:var(--white);box-shadow:0 2px 6px rgba(0,0,0,.2);display:flex;align-items:center;justify-content:center}
.card .brand{font-size:9.5px;gap:5px;letter-spacing:.02em}
.card .brand__square{width:8px;height:8px}
.letter{position:absolute;left:22px;top:105px;width:170px}
.letter h2{font-weight:600;font-size:14px;line-height:1.35;color:var(--ink-dark);margin-bottom:14px;white-space:nowrap;position:relative;z-index:2}
.letter p{font-weight:300;font-size:8.5px;line-height:1.55;color:var(--ink-soft);margin-bottom:10px;text-align:justify}
.signature{width:100px;height:36px;background:linear-gradient(90deg,#ececec,#dedede);margin:8px 0 10px}
.signer{font-weight:600;font-size:10px;color:var(--ink-dark)}
.signer-role{font-weight:300;font-size:9px;color:var(--ink-soft)}
.portrait{position:absolute;right:0;top:150px;width:150px;height:312px;background:linear-gradient(180deg,#d8d3ce 0%,#6e6a68 45%,#3b3a3b 100%)}
.panel--taupe{background:var(--taupe);color:var(--white)}
.claim{position:absolute;left:0;right:0;top:215px;text-align:center}
.claim h3{font-weight:600;font-size:26px;letter-spacing:.08em}
.claim p{font-weight:300;font-size:12px;margin-top:8px}
.contact{position:absolute;left:30px;top:345px;display:flex;flex-direction:column;gap:10px;z-index:2}
.contact li{list-style:none;display:flex;align-items:center;gap:9px;font-size:9px;color:var(--ink)}
.contact svg{width:18px;height:18px;flex:none}
.outside-pattern{position:absolute;left:0;right:0;bottom:48px;height:70px;background:linear-gradient(180deg,var(--paper),#e3e3e3)}
.cover-logo{position:absolute;inset:0;display:flex;align-items:center;justify-content:center}
.cover-logo .brand{font-size:20px}
</style>
</head>
<body>

<section class="spread spread--inside">
  <div class="panel">
    <div class="glass-art" role="img" aria-label="Grafik aus gestaffelten Glasscheiben mit Firmenzeichen">
      <div class="brand"><span class="brand__square"></span>Glaserei Talbunor</div>
    </div>
    <div class="band">www.glaserei-talbunor.de</div>
  </div>
  <div class="panel">
    <div class="center-block">
      <div class="web">www.glaserei-talbunor.de</div>
      <div class="social"><span></span><span></span></div>
    </div>
    <div class="band"></div>
    <div class="pocket">
      <div class="pocket__pattern" role="img" aria-label="Dezentes Monogrammmuster"></div>
      <div class="pocket__mail">info@glaserei-talbunor.de</div>
    </div>
    <div class="card"><div class="brand"><span class="brand__square"></span>Glaserei Talbunor</div></div>
  </div>
  <div class="panel">
    <div class="letter">
      <h2>Herzlich Willkommen<br>bei der Glaserei Talbunor</h2>
      <p>Lorem ipsum dolor sit amet, cons ectetuer adipiscing elit, sed diam nonummy nibh euismod tincidunt ut laoreet dolore magna aliquam erat volutpat.</p>
      <p>Lorem ipsum dolor sit amet, consectetuer adipiscing elit, sed diam nonummy nibh euismod tincidunt ut laoreet dolore magna aliquam erat volutpat. Ut wisi enim ad minim veniam, quis nostrud exerci tation ullamcorper suscipit lobortis nisl ut aliquip.</p>
      <p>Mit freundlichen Grüßen</p>
      <div class="signature" role="img" aria-label="Handschriftliche Unterschrift"></div>
      <div class="signer">Jens Talbunor</div>
      <div class="signer-role">Geschäftsführer</div>
    </div>
    <div class="portrait" role="img" aria-label="Porträtfoto des Geschäftsführers im dunklen Rollkragenpullover"></div>
    <div class="band">Glaserei Talbunor GmbH | Mühlenweg 12 | 24110 Falkstedt</div>
  </div>
</section>

<section class="spread spread--outside">
  <div class="panel panel--taupe">
    <div class="claim">
      <h3>GLAS.</h3>
      <p>So wie es sein soll...</p>
    </div>
  </div>
  <div class="panel">
    <div class="center-block">
      <div class="web">www.glaserei-talbunor.de</div>
      <div class="social"><span></span><span></span></div>
    </div>
    <div class="outside-pattern" role="img" aria-label="Dezentes Monogrammmuster"></div>
    <ul class="contact">
      <li><svg viewBox="0 0 18 18"><rect width="18" height="18" rx="3" fill="#5a5754"/><path d="M9 3.5a3.5 3.5 0 0 0-3.5 3.5c0 2.6 3.5 7 3.5 7s3.5-4.4 3.5-7A3.5 3.5 0 0 0 9 3.5z" fill="#fff"/><circle cx="9" cy="7" r="1.3" fill="#5a5754"/></svg>Mühlenweg 12 | 24110 Falkstedt</li>
      <li><svg viewBox="0 0 18 18"><rect width="18" height="18" rx="3" fill="#5a5754"/><path d="M5 4.5l2 -.5 1.3 2.6-1.2 1a6 6 0 0 0 3.3 3.3l1-1.2 2.6 1.3-.5 2c-4.8.3-8.8-3.7-8.5-8.5z" fill="#fff"/></svg>01234 567890</li>
      <li><svg viewBox="0 0 18 18"><rect width="18" height="18" rx="3" fill="#5a5754"/><rect x="4" y="5.5" width="10" height="7" fill="#fff"/><path d="M4 5.5l5 4 5-4" stroke="#5a5754" stroke-width="1" fill="none"/></svg>info@glaserei-talbunor.de</li>
    </ul>
    <div class="band"></div>
  </div>
  <div class="panel">
    <div class="cover-logo"><div class="brand"><span class="brand__square"></span>Glaserei Talbunor</div></div>
  </div>
</section>

</body>
</html>
```